Business card Zottelgarten

Business card is for a self-employed dog trainer with own dog school. Name and logo of the dog school are available. Color specifications as well. The design should be classy and minimalist, but also modern. An already existing idea would be: Front: Only the logo Back: Contact data

Font styles to use
Serif
Sans Serif
Other font styles liked:
• Trajan Pro

Colors
f78f20

Requirements
Must have
• Name: Margit Wendler-Rasch Title: Dipl. Dog Trainer Contain my logo Follow my font and color preferences (see files)

```html
<!DOCTYPE html>
<html lang="en">
<head>
<meta charset="utf-8">
<title>Zottelgarten – Business Card</title>
<link rel="stylesheet" href="https://fonts.googleapis.com/css2?family=Cinzel:wght@400;600&family=Roboto:wght@400&display=swap">
<style>
  :root {
    --orange: #f78f20;
    --taupe: #7a6a5c;
    --white: #ffffff;
    --ink: #3a3a3a;
    --stage: #1c1c1c;
  }
  * { margin: 0; padding: 0; box-sizing: border-box; }
  html, body { width: 1200px; height: 900px; overflow: hidden; background: var(--stage); }
  .canvas { position: relative; width: 1200px; height: 900px; }

  .card { position: absolute; width: 560px; height: 320px; overflow: hidden; }

  /* Front */
  .card--front { left: 580px; top: 100px; background: var(--orange); }
  .front-mark { position: absolute; left: 385px; top: 70px; width: 150px; height: 150px;
    border-radius: 50%; background: var(--white); }
  .front-name { position: absolute; left: 36px; top: 190px; white-space: nowrap;
    font-family: 'Cinzel', serif; font-weight: 400; font-size: 38px; letter-spacing: 1px;
    color: var(--white); text-transform: uppercase; }
  .front-web { position: absolute; left: 38px; top: 240px; white-space: nowrap;
    font-family: 'Cinzel', serif; font-size: 11px; letter-spacing: 7px;
    color: var(--white); text-transform: uppercase; }

  /* Back */
  .card--back { left: 60px; top: 480px; background: var(--white); }
  .card--back svg.shapes { position: absolute; inset: 0; }
  .holder { position: absolute; left: 28px; top: 16px; font-family: 'Cinzel', serif; color: var(--white); text-transform: uppercase; }
  .holder-name { font-size: 19px; font-weight: 400; letter-spacing: 1px; white-space: nowrap; }
  .holder-title { font-size: 12px; letter-spacing: 1.5px; margin-top: 3px; }

  .contact { position: absolute; left: 28px; top: 112px; font-family: 'Roboto', sans-serif;
    font-size: 13px; color: var(--ink); line-height: 19px; list-style: none; }
  .contact-address { margin-bottom: 6px; }
  .contact li { display: flex; align-items: center; gap: 8px; margin-bottom: 3px; }
  .contact-icon { width: 16px; height: 16px; flex: none; }

  .back-mark-name { position: absolute; left: 340px; top: 178px; width: 200px; text-align: center;
    font-family: 'Cinzel', serif; font-size: 20px; color: var(--white); text-transform: uppercase; white-space: nowrap; }
</style>
</head>
<body>
<main class="canvas">

  <section class="card card--front" aria-label="Card front">
    <div class="front-mark"></div>
    <p class="front-name">Zottelgarten</p>
    <p class="front-web">www.zottelgarten.ch</p>
  </section>

  <section class="card card--back" aria-label="Card back">
    <svg class="shapes" width="560" height="320" viewBox="0 0 560 320" aria-hidden="true">
      <path d="M0 0 H560 V320 H360 Q320 250 330 150 L300 78 H0 Z" fill="var(--taupe)"/>
      <rect x="0" y="78" width="300" height="4" fill="var(--orange)"/>
      <path d="M0 292 H320 Q340 306 352 320 H0 Z" fill="var(--orange)"/>
      <circle cx="440" cy="190" r="118" fill="var(--white)"/>
      <circle cx="440" cy="190" r="108" fill="var(--taupe)"/>
      <circle cx="440" cy="190" r="100" fill="none" stroke="var(--white)" stroke-width="2"/>
    </svg>

    <header class="holder">
      <h1 class="holder-name">Margit Wendler-Rasch</h1>
      <p class="holder-title">Dipl. Hundetrainerin</p>
    </header>

    <ul class="contact">
      <li class="contact-address">42 Meadowbrook Lane<br>Suite 210, Millbrook, NJ</li>
      <li>
        <svg class="contact-icon" viewBox="0 0 16 16"><circle cx="8" cy="8" r="8" fill="var(--taupe)"/><path d="M5 4h2l1 2-1 1a5 5 0 0 0 2 2l1-1 2 1v2c-4 0-7-3-7-7z" fill="var(--white)"/></svg>
        27 10 415 7730
      </li>
      <li>
        <svg class="contact-icon" viewBox="0 0 16 16"><circle cx="8" cy="8" r="8" fill="var(--taupe)"/><rect x="5.5" y="3.5" width="5" height="9" rx="1" fill="var(--white)"/></svg>
        27 82 631 5094
      </li>
      <li>
        <svg class="contact-icon" viewBox="0 0 16 16"><circle cx="8" cy="8" r="8" fill="var(--taupe)"/><rect x="4" y="5" width="8" height="6" fill="var(--white)"/><path d="M4 5l4 3 4-3" fill="none" stroke="var(--taupe)" stroke-width="1"/></svg>
        margit@zottelgarten.ch
      </li>
    </ul>

    <p class="back-mark-name">Zottelgarten</p>
  </section>

</main>
</body>
</html>
```